" Panificadora e confeitaria que atua na venda de café expresso, paes, bolos, doces e mercearia em geral (conveniência). Empresa localizada no Litoral (Praia) com alto fluxo de pessoas, e atualmente atua no mesmo segmento com o nome de "Panificadora e Confeitaria Nelu"(na minha opiniao um nome fraco). No local funciona padaria a 13 anos e somos o terceiro dono. O primeiro dono trabalhou por 10 anos o segundo por 2 anos e meio. Eu sou Padeiro e Confeiteiro formado em Engenharia de Alimentos. Assumimos o negocio em 01/01/2014. "

```html
<!DOCTYPE html>
<html lang="pt-BR">
<head>
<meta charset="utf-8">
<title>Casa Nelu – Identidade Visual</title>
<link rel="stylesheet" href="https://fonts.googleapis.com/css2?family=Cinzel:wght@400;700&family=Lato:wght@400;700&display=swap">
<style>
:root{
  --stage:#3b1419;
  --cream:#f4e8d6;
  --cream-dark:#ecdcc5;
  --wine:#5b1f2a;
  --wine-deep:#45141d;
  --wine-soft:#7a3a45;
  --line:#cdb79c;
  --photo:#b89580;
}
*{box-sizing:border-box;margin:0;padding:0}
html,body{width:1200px;height:1200px;overflow:hidden}
body{background:var(--stage);position:relative;font-family:"Lato",sans-serif;color:var(--wine)}
.piece{position:absolute;overflow:hidden}
.cream{background:var(--cream)}
.wine{background:var(--wine);color:var(--cream)}

/* brand lockup */
.brand{display:flex;flex-direction:column;align-items:center;text-align:center}
.brand__dot{border-radius:50%;background:var(--wine)}
.brand__name{font-family:"Cinzel",serif;font-weight:700;color:var(--wine);line-height:1.1;white-space:nowrap}
.brand__tag{font-family:"Cinzel",serif;letter-spacing:.2em;color:var(--wine-soft);white-space:nowrap}
.brand--xl .brand__dot{width:22px;height:22px;margin-bottom:10px}
.brand--xl .brand__name{font-size:34px}
.brand--xl .brand__tag{font-size:12px;margin-top:4px}
.brand--md .brand__dot{width:14px;height:14px;margin-bottom:6px}
.brand--md .brand__name{font-size:22px}
.brand--md .brand__tag{font-size:9px;margin-top:3px}
.brand--sm .brand__dot{width:9px;height:9px;margin-bottom:4px}
.brand--sm .brand__name{font-size:14px}
.brand--sm .brand__tag{font-size:6px;margin-top:2px}

.center{position:absolute;left:0;right:0;display:flex;justify-content:center}

/* business card */
.card{left:40px;width:400px;height:230px}
.card--front{top:40px}
.card--front .center{top:58px}
.card--back{top:300px;padding:24px 30px;text-align:center}
.card__name{font-family:"Cinzel",serif;font-size:24px;margin-top:10px}
.card__role{font-family:"Cinzel",serif;font-size:11px;letter-spacing:.25em;margin-top:2px}
.rule{height:1px;background:var(--line);opacity:.6;margin:12px auto;width:70%}
.card__info{font-size:11px;line-height:1.65;letter-spacing:.04em}
.card__addr{font-size:9px;margin-top:10px;letter-spacing:.05em;opacity:.85}

/* screen wallpaper */
.wallpaper{left:480px;top:40px;width:680px;height:230px}
.wallpaper svg{position:absolute;inset:0}
.wallpaper .center{top:44px}

/* notes */
.note{top:300px;width:213px;height:260px}
.note--logo{left:480px}
.note--logo .center{top:70px}
.note--lined{left:713px;padding:34px 18px}
.note--lined .ln{height:1px;background:var(--line);margin-bottom:17px}
.note--dark{left:946px;padding:24px 16px;display:flex;flex-direction:column;justify-content:flex-end;text-align:right}
.note--dark p{font-size:8px;line-height:1.6;letter-spacing:.04em}
.note--dark .foot{height:24px;margin:10px -16px -24px;background:var(--wine-deep)}

/* letterheads */
.letter{top:600px;width:382px;height:540px}
.letter--a{left:40px}
.letter--b{left:450px}
.letter__ornament{position:absolute;right:0;bottom:50px;width:190px;height:260px;background:radial-gradient(ellipse at 100% 60%,var(--cream-dark) 0%,rgba(236,220,197,0) 70%)}
.letter--a .center{top:36px}
.letter__foot{position:absolute;left:0;right:0;bottom:0;height:50px;background:var(--wine);color:var(--cream);display:flex;justify-content:space-between;align-items:center;padding:0 22px;font-size:7.5px;line-height:1.6;letter-spacing:.03em}
.letter__head{position:absolute;left:0;right:0;top:0;height:68px;display:flex;align-items:center;padding:0 22px;gap:16px;border-bottom:2px solid var(--wine)}
.letter__meta{font-family:"Cinzel",serif;font-size:10px;line-height:1.5}
.letter__meta small{font-family:"Lato",sans-serif;font-size:7px;display:block}

/* ID badges */
.badge{top:740px;width:140px;height:260px;border-radius:6px}
.badge--front{left:860px}
.badge--front .center{top:18px}
.badge__photo{position:absolute;left:34px;top:84px;width:72px;height:86px;background:linear-gradient(160deg,var(--photo),#8a6a5a);border:2px solid var(--wine)}
.badge__lower{position:absolute;left:0;right:0;bottom:0;height:80px;background:var(--wine);padding:12px 12px 0}
.pill{height:20px;border-radius:4px;background:var(--cream);color:var(--wine);font-family:"Cinzel",serif;font-size:8.5px;display:flex;align-items:center;justify-content:center;letter-spacing:.05em;margin-bottom:7px}
.pill--dark{background:var(--wine-deep);color:var(--cream);border:1px solid var(--cream)}
.badge--back{left:1020px;padding:14px 12px}
.field__label{font-family:"Cinzel",serif;font-size:8.5px;color:var(--cream)}
.field__box{height:12px;background:var(--cream);border-radius:2px;margin:3px 0 9px}
.badge--back .phones{font-size:6.5px;text-align:center;line-height:1.5;margin-top:4px}
.badge--back .brand__name,.badge--back .brand__tag{color:var(--cream)}
.badge--back .brand__dot{background:var(--cream)}
</style>
</head>
<body>

<section class="piece card card--front cream">
  <div class="center">
    <div class="brand brand--xl"><span class="brand__dot"></span><span class="brand__name">Casa Nelu</span><span class="brand__tag">Pães e Doces</span></div>
  </div>
</section>

<section class="piece card card--back wine">
  <h2 class="card__name">Nome Sobrenome</h2>
  <p class="card__role">CARGO</p>
  <div class="rule"></div>
  <p class="card__info">(400) 0000-0000 | (400) 0000-0000<br>contato@casanelu.com.br<br>www.casanelu.com.br</p>
  <p class="card__addr">Endereço Completo, 000 - Bairro - Cidade Estado</p>
</section>

<section class="piece wallpaper cream">
  <svg viewBox="0 0 680 230" preserveAspectRatio="none">
    <path d="M0 230 L0 205 C200 215 430 180 680 95 L680 230 Z" fill="var(--wine)"/>
    <path d="M0 200 C220 205 440 165 680 80" fill="none" stroke="var(--wine-soft)" stroke-width="2"/>
  </svg>
  <div class="center">
    <div class="brand brand--xl"><span class="brand__dot"></span><span class="brand__name">Casa Nelu</span><span class="brand__tag">Pães e Doces</span></div>
  </div>
</section>

<section class="piece note note--logo cream">
  <div class="center">
    <div class="brand brand--md"><span class="brand__dot"></span><span class="brand__name">Casa Nelu</span><span class="brand__tag">Pães e Doces</span></div>
  </div>
</section>
<section class="piece note note--lined cream">
  <div class="ln"></div><div class="ln"></div><div class="ln"></div><div class="ln"></div><div class="ln"></div><div class="ln"></div><div class="ln"></div><div class="ln"></div><div class="ln"></div><div class="ln"></div><div class="ln"></div>
</section>
<section class="piece note note--dark wine">
  <p>(400) 0000-0000 | (400) 0000-0000<br>contato@casanelu.com.br<br>www.casanelu.com.br</p>
  <p style="margin-top:6px">Endereço Completo, 000<br>Bairro - Cidade Estado</p>
  <div class="foot"></div>
</section>

<section class="piece letter letter--a cream">
  <div class="letter__ornament" role="img" aria-label="Ornamento decorativo suave da marca"></div>
  <div class="center">
    <div class="brand brand--sm"><span class="brand__dot"></span><span class="brand__name">Casa Nelu</span><span class="brand__tag">Pães e Doces</span></div>
  </div>
  <footer class="letter__foot">
    <span>(400) 0000-0000<br>(400) 0000-0000</span>
    <span>contato@casanelu.com.br<br>www.casanelu.com.br</span>
    <span>Endereço Completo, 000<br>Bairro - Cidade Estado</span>
  </footer>
</section>

<section class="piece letter letter--b cream">
  <div class="letter__ornament" role="img" aria-label="Ornamento decorativo suave da marca"></div>
  <header class="letter__head">
    <div class="brand brand--sm"><span class="brand__dot"></span><span class="brand__name">Casa Nelu</span><span class="brand__tag">Pães e Doces</span></div>
    <div class="letter__meta">Nome Completo<small>(400) 0000-0000 | (400) 0000-0000</small><small>contato@casanelu.com.br</small></div>
  </header>
  <footer class="letter__foot">
    <span>(400) 0000-0000<br>(400) 0000-0000</span>
    <span>contato@casanelu.com.br<br>www.casanelu.com.br</span>
    <span>Endereço Completo, 000<br>Bairro - Cidade Estado</span>
  </footer>
</section>

<section class="piece badge badge--front cream">
  <div class="center">
    <div class="brand brand--sm"><span class="brand__dot"></span><span class="brand__name">Casa Nelu</span><span class="brand__tag">Pães e Doces</span></div>
  </div>
  <div class="badge__photo" role="img" aria-label="Foto do funcionário"></div>
  <div class="badge__lower">
    <div class="pill">Nome Sobrenome</div>
    <div class="pill pill--dark">Cargo</div>
  </div>
</section>

<section class="piece badge badge--back wine">
  <p class="field__label">Nome Completo:</p><div class="field__box"></div>
  <p class="field__label">CPF:</p><div class="field__box"></div>
  <p class="field__label">RG:</p><div class="field__box"></div>
  <p class="field__label">Data de Admissão:</p><div class="field__box"></div>
  <p class="phones">(400) 0000-0000 | (400) 0000-0000<br>contato@casanelu.com.br</p>
  <div class="brand brand--sm" style="margin-top:8px"><span class="brand__dot"></span><span class="brand__name">Casa Nelu</span><span class="brand__tag">Pães e Doces</span></div>
</section>

</body>
</html>
```